Custome made to measure suit brochure

Company info
Northern Heron Supply Company Ltd.
Import and export company based in Vancouver BC, Canada.

Project Scope
We need to have a brochure developed that will help us sell our custom made to measure suits from Asia (China and India) to North America.

We are not picky on the number of pages, we are looking for a brochure that best displays the needed information.
We don’t have any pictures taken, we are hoping that stock photos can be used or the winning bid will provide the photos.
Attached is our company logo and name, the attachments has 4 or 5 examples, the logo that is being used is the logo that is red and white only.

Target market is the university or college student and young professionals.
We are looking to sell the suit based on best value. Our suit is 3 to 4 times cheaper than a custom made suit made in North America.
Custom made suits make the wearer look amazing, as compared to an off the rack suit.
Custom made suits are available from $399 and up.
Vests, shirts, pants, skirts, jackets, monogramed, horn buttons, canvas and half canvas suits, pocket squares, silk and paisley linings are all available.
Available in Wool, cotton, linen, and a cotton/cashmere blend
We want the client to call us to set up a free appointment to take their measurements
100% satisfaction or your money back.
Brochure should be easy to read and understand at a quick glance.

Target Market(s)

college, university students and young professionals

Industry/Entity Type

It Company

Contact Information for Business Card

Colin Ferrase
President, Northern Heron Supply Company Ltd.
1.604.555.0192
colin@nohesc.ca
www.nohesc.ca

Font styles to use
Serif

Colors
ec1f27

Requirements
Must have
• easy to read
• professional format

```html
<!DOCTYPE html>
<html lang="en">
<head>
<meta charset="utf-8">
<title>Northern Heron Supply Co — Custom Suit Brochure</title>
<link href="https://fonts.googleapis.com/css2?family=Oswald:wght@300;400;500&display=swap" rel="stylesheet">
<style>
:root{
  --stage:#272727;
  --crimson:#cc1d4a;
  --crimson-dark:#b5163f;
  --gold:#f3d35b;
  --orange:#f2a01c;
  --ink:#3a3a3a;
  --grey:#5a5a5a;
  --white:#ffffff;
  --photo-grey:#c9c9cf;
}
*{margin:0;padding:0;box-sizing:border-box}
html,body{width:968px;height:1200px;overflow:hidden;background:var(--stage)}
body{position:relative;font-family:"Oswald",sans-serif;font-weight:300}
.abs{position:absolute}
.spread{position:absolute;left:79px;width:818px;height:529px;overflow:hidden}
.spread-outside{top:29px;background:var(--white)}
.spread-inside{top:608px;height:528px;background:var(--white)}
.body-copy{font-size:8.4px;line-height:11.4px;text-align:justify}
/* outside */
.left-panel{left:0;top:0;width:408px;height:529px;background:var(--crimson)}
.store-card{left:6px;top:6px;width:198px;height:346px;background:var(--gold);padding:8px 12px;color:var(--ink)}
.store-card h2{font-weight:400;font-size:20px;line-height:24px;color:#222}
.store-photo{width:173px;height:99px;margin:8px 0 12px;border:2px solid var(--white);background:linear-gradient(135deg,#8c8a86,#d8d4cc 55%,#6e6a64)}
.store-card p{margin-bottom:9px}
.promise{left:210px;top:12px;width:190px;color:var(--gold);font-weight:400;font-size:22px;line-height:25px;text-align:center}
.promise span{display:block;font-size:21px}
.history{left:219px;top:78px;width:176px;color:var(--white)}
.history h2{font-weight:400;font-size:20px;margin-bottom:9px}
.history p{margin-bottom:10px;color:#fbe7ec}
.contact{left:16px;top:376px;width:200px;color:var(--white)}
.contact h2{font-weight:400;font-size:17px;margin-bottom:18px}
.contact-row{display:flex;align-items:flex-start;gap:10px;font-size:11px;line-height:14px;margin-bottom:15px}
.contact-row svg{flex:none;margin-top:1px}
.brand{left:408px;top:0;width:410px;height:91px;background:var(--white);display:flex;align-items:center;justify-content:flex-end;padding-right:10px;gap:10px}
.brand-mark{width:34px;height:34px;border-radius:50%;background:var(--crimson)}
.brand-name{font-weight:400;font-size:20px;line-height:24px;color:var(--crimson)}
.brand-rule{left:408px;top:91px;width:410px;height:4px;background:var(--crimson)}
.hero-photo{left:408px;top:95px;width:410px;height:323px;background:linear-gradient(90deg,#b7b8bf,#e2e3e7 45%,#c4c5cb)}
.hero-band{left:408px;top:418px;width:410px;height:111px;background:var(--crimson)}
.offer-gold{left:491px;top:408px;width:315px;height:118px;background:var(--gold)}
.offer{left:506px;top:418px;width:312px;height:111px;background:var(--crimson);padding:10px 10px 0 11px;color:var(--white)}
.offer h3{font-weight:400;font-size:24px;line-height:31px}
.offer .web{font-size:11px;margin-top:13px;font-weight:400}
/* inside */
.products-title{left:26px;top:26px;font-weight:400;font-size:20px;color:var(--crimson)}
.products-intro{left:26px;top:59px;width:335px;color:var(--grey);font-size:8.2px;line-height:11.4px}
.round-photo{border-radius:50%;border:1.5px solid var(--crimson)}
.vest-photo{left:18px;top:119px;width:131px;height:131px;background:radial-gradient(circle at 50% 45%,#8b8d91,#3a3b3e 70%)}
.shoe-photo{left:257px;top:282px;width:131px;height:131px;background:radial-gradient(circle at 50% 55%,#3a3a3a,#f2f2f2 72%)}
.product{width:226px;color:var(--grey)}
.product h4{font-weight:400;font-size:11.5px;color:var(--orange);margin-bottom:2px}
.product p{font-size:8px;line-height:11.4px}
.p1{left:157px;top:114px}
.p2{left:157px;top:190px}
.p3{left:17px;top:275px}
.p4{left:17px;top:352px}
.callout-gold{left:376px;top:6px;width:188px;height:76px;background:var(--gold)}
.callout{left:370px;top:0;width:188px;height:75px;background:var(--crimson);color:var(--white);font-weight:400;font-size:10.5px;line-height:14px;text-align:center;padding:13px 14px 0}
.sitting-photo{left:560px;top:8px;width:250px;height:156px;background:linear-gradient(180deg,#f4f6f8 0%,#8fb2dc 40%,#2c2c30 75%,#f4f6f8 100%);opacity:.8;border-radius:8px}
.why-title{left:424px;top:132px;font-weight:400;font-size:19px;color:var(--crimson)}
.reason{left:423px;width:380px;display:flex;gap:10px;align-items:flex-start}
.reason .icon{flex:none;width:50px;height:50px;border-radius:50%;border:1.5px solid var(--crimson);display:flex;align-items:center;justify-content:center}
.reason p{font-size:8px;line-height:11.2px;color:var(--grey);margin-top:4px}
.r1{top:172px}
.r2{top:237px}
.r3{top:299px}
.duo-photo{left:431px;top:366px;width:174px;height:162px;background:linear-gradient(180deg,#f1f1f1 0%,#bfa58e 35%,#2a2b2f 70%,#1f2024 100%)}
.cta-gold{left:611px;top:419px;width:201px;height:109px;background:var(--gold)}
.cta{left:607px;top:427px;width:211px;height:101px;background:var(--crimson);color:var(--white);text-align:center;padding-top:12px}
.cta p{font-weight:400;font-size:12.5px;line-height:17px}
.cta strong{display:block;font-weight:400;font-size:34px;line-height:40px;margin-top:1px}
.fabric-rule{left:9px;top:445px;width:163px;height:10px;background:var(--crimson)}
.fabric{left:0;top:452px;width:172px;height:76px;background:var(--gold);color:#222;font-weight:400;font-size:12.5px;line-height:17px;text-align:center;padding-top:7px}
.quote-mark{left:204px;top:444px;font-weight:500;font-size:42px;line-height:42px;color:var(--crimson)}
.quote{left:232px;top:458px;width:164px;font-size:8px;line-height:11.2px;color:var(--crimson)}
</style>
</head>
<body>

<section class="spread spread-outside">
  <div class="abs left-panel"></div>

  <div class="abs store-card">
    <h2>Our Store</h2>
    <div class="store-photo" role="img" aria-label="Photo of the store interior with suits on racks"></div>
    <p class="body-copy">Duis autem vel eum iriure dolor in hendrerit in vulputate velit esse molestie consequat, vel illum dolore eu feugiat nulla facilisis at vero eros et accumsan et iusto odio dignissim qui blandit praesent luptatum zzril delenit augue duis dolore te feugait nulla facilisi. Nam liber tempor cum soluta nobis eleifend option congue nihil imperdiet doming id quod mazim placerat facer possim assum.</p>
    <p class="body-copy">Typi non habent claritatem insitam; est usus legentis in iis qui facit eorum claritatem. Investigationes demonstraverunt lectores legere me lius quod ii legunt saepius. Claritas est etiam processus dynamicus, qui sequitur mutationem consue.</p>
  </div>

  <div class="abs promise">100% SATISFACTION! <span>OR YOUR MONEY BACK.</span></div>

  <div class="abs history">
    <h2>Our History</h2>
    <p class="body-copy">Lorem ipsum dolor sit amet, consectetuer adipiscing elit, sed diam nonummy nibh euismod tincidunt ut laoreet dolore magna aliquam erat volutpat. Ut wisi enim ad minim veniam, quis nostrud exerci tation ullamcorper suscipit lobortis nisl ut aliquip ex ea commodo consequat.</p>
    <p class="body-copy">Duis autem vel eum iriure dolor in hendrerit in vulputate velit esse molestie consequat, vel illum dolore eu feugiat nulla facilisis at vero eros et accumsan et iusto odio dignissim qui blandit praesent luptatum zzril delenit augue duis dolore te feugait nulla facilisi. Nam liber tempor cum soluta nobis eleifend option congue nihil imperdiet doming id quod mazim placerat facer possim assum.</p>
    <p class="body-copy">Typi non habent claritatem insitam; est usus legentis in iis qui facit eorum claritatem. Investigationes demonstraverunt lectores legere me lius quod ii legunt saepius. Claritas est etiam processus dynamicus, qui sequitur mutationem consue.</p>
  </div>

  <div class="abs contact">
    <h2>Contact Us</h2>
    <div class="contact-row">
      <svg width="11" height="14" viewBox="0 0 11 14"><path d="M5.5 0A5.5 5.5 0 0 0 0 5.5C0 9.5 5.5 14 5.5 14S11 9.5 11 5.5A5.5 5.5 0 0 0 5.5 0zm0 7.7a2.2 2.2 0 1 1 0-4.4 2.2 2.2 0 0 1 0 4.4z" fill="#fff"/></svg>
      <span>1280 Alder Street #400<br>Vancouver, BC V6B 2L4</span>
    </div>
    <div class="contact-row">
      <svg width="11" height="14" viewBox="0 0 11 14"><rect x="1" y="0" width="9" height="14" rx="1.5" fill="#fff"/><rect x="2.5" y="2" width="6" height="8.5" fill="#cc1d4a"/><circle cx="5.5" cy="12.2" r=".9" fill="#cc1d4a"/></svg>
      <span>(604) 555-0147</span>
    </div>
    <div class="contact-row">
      <svg width="13" height="10" viewBox="0 0 13 10"><rect width="13" height="10" rx="1" fill="#fff"/><path d="M0.5 1l6 4.5 6-4.5" stroke="#cc1d4a" stroke-width="1.2" fill="none"/></svg>
      <span>info@nohesc.ca</span>
    </div>
  </div>

  <div class="abs brand">
    <div class="brand-mark"></div>
    <div class="brand-name">Northern Heron<br>Supply Co</div>
  </div>
  <div class="abs brand-rule"></div>
  <div class="abs hero-photo" role="img" aria-label="Photo of a young man in a black tuxedo with a bow tie"></div>
  <div class="abs hero-band"></div>
  <div class="abs offer-gold"></div>
  <div class="abs offer">
    <h3>Custom made suits are available<br>from $399 and up</h3>
    <div class="web">www.nohesc.ca</div>
  </div>
</section>

<section class="spread spread-inside">
  <h2 class="abs products-title">Our Products</h2>
  <p class="abs products-intro">Lorem ipsum dolor sit amet, consectetuer adipiscing elit, sed diam nonummy nibh euismod tincidunt ut laoreet dolore magna aliquam erat volutpat. Ut wisi enim ad minim veniam, quis nostrud exerci tation ullamcorper suscipit lobortis nisl ut aliquip ex ea commodo consequat.</p>

  <div class="abs round-photo vest-photo" role="img" aria-label="Photo of a man in a grey vest and tie"></div>
  <div class="abs product p1"><h4>PRODUCT 1</h4><p>Lorem ipsum dolor sit amet, consectetuer adipiscing elit, sed diam nonummy nibh euismod tincidunt ut laoreet dolore magna aliquam erat volutpat. Ut wisi enim ad minim veniam, quis nostrud exerci tation ullamcorper suscipit lobortis nisl ut aliquip ex ea commodo consequat.</p></div>
  <div class="abs product p2"><h4>PRODUCT 2</h4><p>Lorem ipsum dolor sit amet, consectetuer adipiscing elit, sed diam nonummy nibh euismod tincidunt ut laoreet dolore magna aliquam erat volutpat. Ut wisi enim ad minim veniam, quis nostrud exerci tation ullamcorper suscipit lobortis nisl ut aliquip ex ea commodo consequat.</p></div>
  <div class="abs product p3"><h4>PRODUCT 3</h4><p>Lorem ipsum dolor sit amet, consectetuer adipiscing elit, sed diam nonummy nibh euismod tincidunt ut laoreet dolore magna aliquam erat volutpat. Ut wisi enim ad minim veniam, quis nostrud exerci tation ullamcorper suscipit lobortis nisl ut aliquip ex ea commodo consequat.</p></div>
  <div class="abs product p4"><h4>PRODUCT 4</h4><p>Lorem ipsum dolor sit amet, consectetuer adipiscing elit, sed diam nonummy nibh euismod tincidunt ut laoreet dolore magna aliquam erat volutpat. Ut wisi enim ad minim veniam, quis nostrud exerci tation ullamcorper suscipit lobortis nisl ut aliquip ex ea commodo consequat.</p></div>
  <div class="abs round-photo shoe-photo" role="img" aria-label="Photo of legs in suit trousers and black leather shoes"></div>

  <div class="abs callout-gold"></div>
  <div class="abs callout">Custom made suits make the wearer look amazing, as compared to an off the rack suit.</div>
  <div class="abs sitting-photo" role="img" aria-label="Photo of a smiling man in a blue shirt and tie sitting on the floor"></div>

  <h2 class="abs why-title">Why Choose Us?</h2>
  <div class="abs reason r1">
    <div class="icon"><svg width="22" height="22" viewBox="0 0 22 22"><rect x="1" y="9" width="5" height="12" fill="#cc1d4a"/><path d="M8 9l4-8c2 0 3 1 2.5 3L13.5 8H20c1.2 0 2 1 1.7 2.2l-2 9C19.5 20.3 18.7 21 17.6 21H8z" fill="#cc1d4a"/></svg></div>
    <p>Lorem ipsum dolor sit amet, consectetuer adipiscing elit, sed diam nonummy nibh euismod tincidunt ut laoreet dolore magna aliquam erat volutpat. Ut wisi enim ad minim veniam, quis nostrud exerci tation ullamcorper suscipit lobortis nisl ut aliquip ex ea commodo consequat.</p>
  </div>
  <div class="abs reason r2">
    <div class="icon"><svg width="24" height="20" viewBox="0 0 24 20"><rect x="1" y="5" width="22" height="13" fill="#cc1d4a"/><rect x="4" y="1" width="18" height="3" fill="#cc1d4a"/><circle cx="12" cy="11.5" r="3.5" fill="#fff"/><rect x="3" y="7" width="3" height="2" fill="#fff"/><rect x="18" y="14" width="3" height="2" fill="#fff"/></svg></div>
    <p>Lorem ipsum dolor sit amet, consectetuer adipiscing elit, sed diam nonummy nibh euismod tincidunt ut laoreet dolore magna aliquam erat volutpat. Ut wisi enim ad minim veniam, quis nostrud exerci tation ullamcorper suscipit lobortis nisl ut aliquip ex ea commodo consequat.</p>
  </div>
  <div class="abs reason r3">
    <div class="icon"><svg width="22" height="22" viewBox="0 0 22 22"><path d="M2 3l6-2 3 4 3-4 6 2v18H2z" fill="#cc1d4a"/><path d="M8 1l3 10 3-10-3 4z" fill="#fff"/><path d="M9 6l2 2 2-2-1 3h-2z" fill="#cc1d4a"/></svg></div>
    <p>Lorem ipsum dolor sit amet, consectetuer adipiscing elit, sed diam nonummy nibh euismod tincidunt ut laoreet dolore magna aliquam erat volutpat. Ut wisi enim ad minim veniam, quis nostrud exerci tation ullamcorper suscipit lobortis nisl ut aliquip ex ea commodo consequat.</p>
  </div>

  <div class="abs duo-photo" role="img" aria-label="Photo of a young man and woman in business suits"></div>
  <div class="abs cta-gold"></div>
  <div class="abs cta">
    <p>Call us to set up a free appointment<br>to take your measurements!</p>
    <strong>123 456 7890</strong>
  </div>

  <div class="abs fabric-rule"></div>
  <div class="abs fabric">Available in Wool, cotton,<br>linen, and a cotton<br>/cashmere blend</div>
  <div class="abs quote-mark">“</div>
  <p class="abs quote">Lorem ipsum dolor sit amet, consectetuer adipiscing elit, sed diam nonummy nibh euismod tincidunt ut laoreet dolore magna aliquam erat volutpat. Ut wisi enim ad minim veniam, quis nostrud exerci tation ullamcorper suscipit lobortis nisl ut aliquip ex ea commodo consequat.</p>
</section>

</body>
</html>
```